Business card design for counselling and psychotherapy practice

I am seeking a business card for a new venture into private practice. I am based in Brisbane Qld Australia. I provide holistic counselling and psychotherapy to individuals and groups.
Some words that describe the underpinnings of this practice would include: being, becoming, awareness, wholeness, contact, safety, acceptance, relationship, gestalt, paradox, interconnected, nature, process.
I would like to see designs that include earth colours.
The overall design should communicate safety and a curiosity of being and becoming.
Target Market(s)
this design is marketed toward women, professionals, lesbian, transgender, mothers
Industry/Entity Type
Safety
Contact Information for Business Card
Willow & Tide
Counselling and Psychotherapy
Maren Olcott
ph: 0417382905
email: maren.willow&tide@quietmail.net
www.willow&tidecounselling&psychotherapy.net
Logo styles of interest
Abstract Logo
Look and feel
Each slider illustrates characteristics of the customer's brand and the style your logo design should communicate.

```html
<!DOCTYPE html>
<html lang="en">
<head>
<meta charset="utf-8">
<title>Willow &amp; Tide – Business Card</title>
<link rel="stylesheet" href="https://fonts.googleapis.com/css2?family=Cinzel:wght@400&family=Jost:wght@400&display=swap">
<style>
  :root {
    --rust: #b4553a;
    --slate: #6b6a60;
    --ink: #2e2e2e;
    --grey: #5c5c5c;
    --paper: #ffffff;
    --backdrop: #ededed;
  }
  * { margin: 0; padding: 0; box-sizing: border-box; }
  html, body { width: 1200px; height: 960px; overflow: hidden; }
  body {
    background: var(--backdrop);
    display: flex;
    align-items: center;
    justify-content: center;
    gap: 60px;
  }
  .card {
    position: relative;
    width: 520px;
    height: 300px;
    background: var(--paper);
    box-shadow: 0 2px 10px rgba(0,0,0,0.12);
    overflow: hidden;
  }

  /* Front */
  .brand {
    position: absolute;
    left: 62px;
    top: 112px;
    display: flex;
    align-items: center;
    gap: 14px;
  }
  .brand-dot {
    width: 40px;
    height: 40px;
    border-radius: 50%;
    background: var(--slate);
    flex: none;
  }
  .brand-name {
    font-family: 'Cinzel', serif;
    font-weight: 400;
    font-size: 30px;
    line-height: 1;
    color: var(--rust);
    letter-spacing: 1px;
  }
  .brand-tagline {
    font-family: 'Cinzel', serif;
    font-size: 11.5px;
    color: var(--slate);
    letter-spacing: 2.6px;
    margin-top: 6px;
  }
  .website {
    position: absolute;
    right: 36px;
    bottom: 28px;
    font-family: 'Jost', sans-serif;
    font-size: 12.5px;
    color: var(--grey);
    letter-spacing: 0.6px;
  }

  /* Back */
  .arc-band { position: absolute; inset: 0; }
  .contact {
    position: absolute;
    right: 34px;
    top: 160px;
    text-align: right;
    font-family: 'Jost', sans-serif;
    color: var(--ink);
  }
  .contact-name {
    font-size: 27px;
    letter-spacing: 3px;
    margin-bottom: 14px;
  }
  .contact-line {
    font-size: 16px;
    letter-spacing: 0.5px;
    line-height: 1.5;
  }
</style>
</head>
<body>

  <section class="card card-front">
    <div class="brand">
      <span class="brand-dot"></span>
      <div>
        <div class="brand-name">Willow &amp; Tide</div>
        <div class="brand-tagline">COUNSELLING AND PSYCHOTHERAPY</div>
      </div>
    </div>
    <p class="website">www.willow&amp;tidecounselling&amp;psychotherapy.net</p>
  </section>

  <section class="card card-back">
    <svg class="arc-band" viewBox="0 0 520 300" width="520" height="300" aria-hidden="true">
      <path d="M38 300 C140 170 300 30 470 0 L520 0 L520 60 C340 55 170 170 82 300 Z" fill="var(--rust)"/>
    </svg>
    <div class="contact">
      <div class="contact-name">MAREN OLCOTT</div>
      <div class="contact-line">Ph: 0417382905</div>
      <div class="contact-line">Email: maren.willow&amp;tide@quietmail.net</div>
    </div>
  </section>

</body>
</html>
```